Harbor Emberlights - Woodwick candles needing a sylish box designed

We need a box designed for our woodwick candles.
I would like to see a box that looks very stylish and I would like the logo to be in a silver foil outlined box (I will include photos of examples). I like a box that has a silver foil edge around it, though not essential. A pattern of some sort would be nice on the box, staying with the wood/beach theme. I will also need to include other information on the back of the box about the candle (can I do this after I see the design?). I need to be able to change the fragrance when needed on the box label. The box size is L105mm W105mm H128mm. I am really open to any ideas. Looking for something very stylish and luxurious looking.
The lids on my candles are silver and the candles have a wooden wick.

Target Market(s)

Department stores and retail shops

Industry/Entity Type

Retail

Colors
ffffff

Requirements
Must have
• Looking for something very stylish and luxurious looking, that will look and fit great in any large department store.
Nice to have
• Wooden look, if possible.
• Clean and crisp look. Very pretty.

```html
<!DOCTYPE html>
<html lang="en">
<head>
<meta charset="utf-8">
<title>Harbor Emberlights – Candle Box Labels</title>
<link rel="stylesheet" href="https://fonts.googleapis.com/css2?family=Cormorant+Garamond:wght@400;500&family=Great+Vibes&display=swap">
<style>
  :root {
    --backdrop: #e0e0e2;
    --paper: #ffffff;
    --silver-dark: #8e8e90;
    --silver-mid: #b9b9bb;
    --silver-light: #ececee;
    --grain-deep: #e6e6e8;
    --grain-soft: #f7f7f8;
    --ink: #9a9a9c;
    --lavender: #d8d8fa;
    --mandarin: #f5d9d2;
    --peppermint: #dcf6f2;
    --divider: #ffffff;
  }
  * { box-sizing: border-box; margin: 0; padding: 0; }
  html, body { width: 1200px; height: 1142px; overflow: hidden; }
  body {
    position: relative;
    background: var(--backdrop);
    font-family: "Cormorant Garamond", Georgia, serif;
  }

  /* Box fronts */
  .box-front {
    position: absolute;
    top: 198px;
    width: 358px;
    height: 362px;
    background: var(--paper);
  }
  .box-front--lavender { left: 19px; }
  .box-front--mandarin,
  .box-front--peppermint {
    background: linear-gradient(90deg, var(--silver-light) 0%, var(--silver-mid) 30%, #f4f4f5 55%, var(--silver-mid) 80%, var(--silver-light) 100%);
  }
  .box-front--mandarin { left: 424px; top: 201px; }
  .box-front--peppermint { left: 814px; top: 201px; }

  .wood-grain {
    position: absolute;
    inset: 7px;
    background:
      linear-gradient(180deg, rgba(255,255,255,0) 0%, rgba(255,255,255,0.7) 72%, rgba(255,255,255,0.2) 100%),
      linear-gradient(90deg, var(--grain-deep) 0%, var(--grain-soft) 18%, var(--grain-deep) 34%, var(--grain-soft) 50%, var(--grain-deep) 66%, var(--grain-soft) 82%, var(--grain-deep) 100%);
  }
  .box-front .label { left: 91px; top: 88px; }

  /* Label */
  .label {
    position: absolute;
    background: var(--paper);
  }
  .label__frame {
    position: absolute;
    border: 3px solid var(--silver-mid);
    border-top-color: var(--silver-light);
    border-left-color: var(--silver-dark);
    border-bottom-color: var(--silver-dark);
  }
  .label__mark {
    position: absolute;
    left: 50%;
    border: 1.5px solid var(--silver-mid);
    border-radius: 50%;
  }
  .label__name {
    position: absolute;
    left: 0; right: 0;
    text-align: center;
    color: var(--ink);
    font-variant: small-caps;
    font-weight: 500;
    white-space: nowrap;
  }
  .label__scent {
    position: absolute;
    left: 0; right: 0;
    text-align: center;
    color: var(--ink);
    text-transform: uppercase;
    font-weight: 500;
  }
  .label__scent--script {
    font-family: "Great Vibes", cursive;
    text-transform: none;
  }
  .label__bar { position: absolute; }
  .label__bar--lavender { background: var(--lavender); }
  .label__bar--mandarin { background: var(--mandarin); }
  .label__bar--peppermint { background: var(--peppermint); }

  /* Small label on box fronts */
  .label--small { width: 178px; height: 182px; }
  .label--small .label__frame { inset: 3px; border-width: 2px; }
  .label--small .label__mark { top: 44px; width: 42px; height: 42px; margin-left: -21px; }
  .label--small .label__name { top: 95px; font-size: 14px; letter-spacing: 0.6px; }
  .label--small .label__scent { top: 145px; font-size: 7px; letter-spacing: 3px; }
  .label--small .label__scent--script { top: 140px; font-size: 11px; letter-spacing: 0; }
  .label--small .label__bar { left: 17px; right: 16px; top: 162px; height: 6px; }

  /* Divider */
  .divider {
    position: absolute;
    left: 0; right: 0;
    top: 740px;
    height: 4px;
    background: var(--divider);
  }

  /* Large flat labels */
  .label--large { width: 291px; height: 291px; top: 806px; }
  .label--large.label--lavender { left: 87px; }
  .label--large.label--mandarin { left: 433px; }
  .label--large.label--peppermint { left: 798px; }
  .label--large .label__frame { inset: 8px; border-width: 3px; }
  .label--large .label__mark { top: 76px; width: 68px; height: 68px; margin-left: -34px; }
  .label--large .label__name { top: 152px; font-size: 23px; letter-spacing: 1px; }
  .label--large .label__scent { top: 231px; font-size: 12px; letter-spacing: 5px; }
  .label--large .label__scent--script { top: 224px; font-size: 18px; letter-spacing: 0; }
  .label--large .label__bar { left: 34px; right: 34px; top: 255px; height: 11px; }
</style>
</head>
<body>

  <section class="box-front box-front--lavender">
    <div class="wood-grain" role="img" aria-label="Soft white wood grain pattern"></div>
    <div class="label label--small">
      <div class="label__frame"></div>
      <div class="label__mark"></div>
      <p class="label__name">Harbor Emberlights</p>
      <p class="label__scent">Lavender</p>
      <div class="label__bar label__bar--lavender"></div>
    </div>
  </section>

  <section class="box-front box-front--mandarin">
    <div class="wood-grain" role="img" aria-label="Soft white wood grain pattern"></div>
    <div class="label label--small">
      <div class="label__frame"></div>
      <div class="label__mark"></div>
      <p class="label__name">Harbor Emberlights</p>
      <p class="label__scent">Mandarin</p>
      <div class="label__bar label__bar--mandarin"></div>
    </div>
  </section>

  <section class="box-front box-front--peppermint">
    <div class="wood-grain" role="img" aria-label="Soft white wood grain pattern"></div>
    <div class="label label--small">
      <div class="label__frame"></div>
      <div class="label__mark"></div>
      <p class="label__name">Harbor Emberlights</p>
      <p class="label__scent label__scent--script">Peppermint</p>
      <div class="label__bar label__bar--peppermint"></div>
    </div>
  </section>

  <div class="divider"></div>

  <section class="label label--large label--lavender">
    <div class="label__frame"></div>
    <div class="label__mark"></div>
    <p class="label__name">Harbor Emberlights</p>
    <p class="label__scent">Lavender</p>
    <div class="label__bar label__bar--lavender"></div>
  </section>

  <section class="label label--large label--mandarin">
    <div class="label__frame"></div>
    <div class="label__mark"></div>
    <p class="label__name">Harbor Emberlights</p>
    <p class="label__scent">Mandarin</p>
    <div class="label__bar label__bar--mandarin"></div>
  </section>

  <section class="label label--large label--peppermint">
    <div class="label__frame"></div>
    <div class="label__mark"></div>
    <p class="label__name">Harbor Emberlights</p>
    <p class="label__scent label__scent--script">Peppermint</p>
    <div class="label__bar label__bar--peppermint"></div>
  </section>

</body>
</html>
```